FBO Nashville 2025

a catchy design to use on instagram and email to market my upcoming dental course called Functional Balanced Orthodontics coming up May 23-24 in Nashville at the Driftwood Harbor . the course is a " 2-day Hands On Workshop" in the uploaded files are some of the ideas we made ourselves in the past but they don't look professional. i also included other peoples post that i like.

```html
<!DOCTYPE html>
<html lang="en">
<head>
<meta charset="utf-8">
<title>FBO Nashville Workshop</title>
<link href="https://fonts.googleapis.com/css2?family=Montserrat:wght@500;800&family=Roboto+Condensed:wght@700;900&display=swap" rel="stylesheet">
<style>
  :root{
    --white:#ffffff;
    --ink:#000000;
    --navy:#243566;
    --blue-light:#5faee8;
    --blue-mid:#3f74ad;
    --blue-deep:#2c3b6f;
    --skin-light:#f0c7b8;
    --skin-deep:#d98b86;
    --sky:#7f93d0;
    --building:#e9ecef;
    --pool:#6f9fc4;
  }
  html,body{margin:0;padding:0;overflow:hidden;background:var(--white);}
  .poster{display:block;width:1200px;height:1198px;}
  .brand-mark{font-family:"Montserrat",sans-serif;font-weight:800;fill:var(--navy);}
  .brand-name{font-family:"Montserrat",sans-serif;font-weight:500;fill:var(--ink);}
  .city{font-family:"Roboto Condensed",sans-serif;font-weight:900;fill:var(--white);}
  .date{font-family:"Roboto Condensed",sans-serif;font-weight:900;fill:var(--ink);}
  .details{font-family:"Roboto Condensed",sans-serif;font-weight:700;fill:var(--white);}
  .info-frame{fill:none;stroke:var(--white);stroke-width:3;}
  .social-dot{fill:none;stroke:var(--white);stroke-width:2.5;}
</style>
</head>
<body>
<svg class="poster" viewBox="0 0 1200 1198" xmlns="http://www.w3.org/2000/svg">
  <defs>
    <linearGradient id="bandGradient" x1="0" y1="0" x2="1" y2="0">
      <stop offset="0" stop-color="var(--blue-light)"/>
      <stop offset="0.45" stop-color="var(--blue-mid)"/>
      <stop offset="1" stop-color="var(--blue-deep)"/>
    </linearGradient>
    <linearGradient id="smileGradient" x1="0" y1="0" x2="1" y2="1">
      <stop offset="0" stop-color="var(--skin-light)"/>
      <stop offset="1" stop-color="var(--skin-deep)"/>
    </linearGradient>
    <linearGradient id="venueGradient" x1="0" y1="0" x2="0" y2="1">
      <stop offset="0" stop-color="var(--sky)"/>
      <stop offset="0.55" stop-color="var(--building)"/>
      <stop offset="1" stop-color="var(--pool)"/>
    </linearGradient>
  </defs>

  <rect class="backdrop" width="1200" height="1198" fill="var(--white)"/>

  <polygon class="photo-smile" role="img" aria-label="Close-up photo of a smile with pink-banded orthodontic braces"
           points="0,0 733,0 568,547 0,600" fill="url(#smileGradient)"/>

  <polygon class="photo-venue" role="img" aria-label="Photo of the Driftwood Harbor rooftop pool and lounge with city skyline"
           points="668,279 1200,279 1200,640 560,640" fill="url(#venueGradient)"/>

  <g class="brand">
    <text class="brand-mark" x="762" y="140" font-size="128" textLength="330" lengthAdjust="spacingAndGlyphs">FBO</text>
    <text class="brand-name" x="764" y="196" font-size="33">Functional Balanced</text>
    <text class="brand-name" x="764" y="238" font-size="33">Orthodontics</text>
  </g>

  <path class="wave-edge" d="M0,612 C180,560 360,510 500,514 C660,518 800,600 950,612 C1060,620 1140,590 1200,578 L1200,1198 L0,1198 Z" fill="var(--ink)"/>
  <path class="blue-band" d="M0,630 C180,578 360,528 500,530 C660,534 800,616 950,628 C1060,636 1140,606 1200,594 L1200,1198 L0,1198 Z" fill="url(#bandGradient)"/>

  <text class="city" x="90" y="850" font-size="292" textLength="1025" lengthAdjust="spacingAndGlyphs">Nashville</text>

  <g class="event-info">
    <rect class="info-frame" x="87" y="882" width="1028" height="186" rx="26"/>
    <line class="info-frame" x1="284" y1="882" x2="284" y2="1068"/>
    <text class="date" x="186" y="969" font-size="82" text-anchor="middle">May</text>
    <text class="date" x="187" y="1037" font-size="68" text-anchor="middle" textLength="140" lengthAdjust="spacingAndGlyphs">23-24</text>
    <text class="details" x="316" y="968" font-size="68" textLength="756" lengthAdjust="spacingAndGlyphs">A 2-day Hands On Workshop</text>
    <text class="details" x="316" y="1037" font-size="68">at the Driftwood Harbor</text>
  </g>

  <g class="social-links">
    <circle class="social-dot" cx="922" cy="1121" r="21"/>
    <circle class="social-dot" cx="986" cy="1121" r="21"/>
    <circle class="social-dot" cx="1051" cy="1121" r="21"/>
    <circle class="social-dot" cx="1115" cy="1121" r="21"/>
  </g>
</svg>
</body>
</html>
```